Staffing Company Website

We need a website for a new company based out of central California called "Harbor Field Staffing". We staff truck drivers for agriculture trucking businesses. We don't want a super corporate feel, we want something that feels more inviting to the kind of person who would work in Agriculture/Trucking while still being professional. Please let me know if you have any questions

```html
<!DOCTYPE html>
<html lang="en">
<head>
<meta charset="UTF-8">
<title>Harbor Field Staffing</title>
<link href="https://fonts.googleapis.com/css2?family=Bebas+Neue&family=Poppins:wght@400;500;600&display=swap" rel="stylesheet">
<style>
:root{
  --ink:#2f3640;
  --ink-soft:#555b63;
  --sand:#ecdcc0;
  --sand-deep:#e2c9a2;
  --card:#efefef;
  --sage:#e8efe5;
  --sage-line:#b9d0b0;
  --white:#ffffff;
  --muted:#6b7078;
}
*{margin:0;padding:0;box-sizing:border-box}
html,body{width:1200px;height:4454px;overflow:hidden}
body{position:relative;background:var(--white);font-family:'Poppins',sans-serif;color:var(--ink)}
.abs{position:absolute}
.display{font-family:'Bebas Neue',sans-serif;font-weight:400;letter-spacing:.5px;line-height:1}
.btn{position:absolute;display:flex;align-items:center;justify-content:center;font-family:'Poppins',sans-serif;font-weight:600;font-size:11.5px;text-transform:uppercase;border-radius:6px;color:var(--ink)}
.btn-outline{border:2px solid var(--ink);background:var(--white)}
.btn-sand{background:var(--sand-deep)}
.photo{position:absolute}

.header-tab{position:absolute;left:0;top:0;z-index:3}
.brand{position:absolute;left:48px;top:20px;z-index:4;display:flex;align-items:center;gap:12px}
.brand-square{width:50px;height:50px;background:var(--ink);border-radius:4px}
.brand-name{font-family:'Poppins',sans-serif;font-weight:600;font-size:14px;line-height:1.2;text-transform:uppercase;color:var(--ink)}
.nav{position:absolute;left:545px;top:35px;width:415px;height:48px;background:var(--white);border-radius:8px;display:flex;align-items:center;justify-content:space-around;padding:0 8px;z-index:4}
.nav a{font-size:12px;color:var(--ink);text-decoration:none;text-transform:uppercase;padding:10px 12px;border-radius:6px}
.nav a.active{background:#e7e7e7;font-weight:600}
.nav-cta{left:977px;top:33px;width:133px;height:50px;z-index:4;background:var(--sand-deep);gap:6px}
.nav-cta .dot{width:12px;height:12px;border-radius:50%;background:var(--ink)}

.hero-photo{left:0;top:0;width:1200px;height:685px;background:linear-gradient(100deg,#4a4a48 0%,#5b5755 30%,#7d2a33 55%,#b0313e 68%,#9f8f86 85%,#c6b9ad 100%)}
.hero-card{left:88px;top:176px;width:277px;height:419px;background:rgba(40,42,44,.82);border-radius:6px}
.hero-rule{left:130px;top:228px;width:3px;height:190px;background:var(--white)}
.hero-title{left:161px;top:225px;color:var(--white);font-size:66px;line-height:1;width:420px}
.hero-sub{left:130px;top:439px;width:400px;color:var(--white);font-size:15px;line-height:1.45}
.hero-btn{left:130px;top:500px;width:133px;height:45px}
.arrow{position:absolute;width:40px;height:40px;border-radius:50%;display:flex;align-items:center;justify-content:center}
.arrow-prev{left:1024px;top:542px;background:rgba(255,255,255,.35)}
.arrow-next{left:1069px;top:542px;background:var(--white)}

.about{left:0;top:685px;width:1200px;height:518px;background:var(--sand)}
.about-img1{left:135px;top:771px;width:152px;height:277px;border-radius:14px;background:linear-gradient(160deg,#9ec6e3 0%,#b9cf6a 45%,#6e7d3a 100%)}
.about-img2{left:299px;top:771px;width:318px;height:277px;border-radius:14px;background:linear-gradient(165deg,#b7cfe1 0%,#a8b868 40%,#6c7a35 75%,#8a7a4a 100%)}
.section-title{font-family:'Bebas Neue',sans-serif;font-size:34px;line-height:1.05;color:var(--ink)}
.about-title{left:669px;top:766px}
.body-copy{font-size:12.5px;line-height:20.5px;color:var(--ink-soft)}
.about-copy{left:669px;top:856px;width:410px}
.about-btn{left:669px;top:1003px;width:132px;height:43px;background:transparent}

.services-title{left:0;top:1213px;width:1200px;text-align:center}
.service{position:absolute;top:1279px;width:294px;height:329px;background:var(--card);border-radius:16px;padding:33px 46px}
.service.featured{background:var(--sage);border-bottom:3px solid var(--sage-line)}
.service-icon{width:86px;height:86px;background:var(--white);border-radius:10px;display:flex;align-items:center;justify-content:center}
.service-icon div{width:56px;height:56px;border-radius:8px;background:#e4e4e4}
.service h3{font-family:'Bebas Neue',sans-serif;font-weight:400;font-size:19px;line-height:1.05;margin-top:30px;letter-spacing:.4px}
.service p{font-size:11.5px;line-height:19px;color:var(--ink-soft);margin-top:16px}

.drivers-title{left:218px;top:1727px}
.drivers-copy{left:218px;top:1815px;width:360px}
.drivers-btn{left:218px;top:1945px;width:131px;height:45px;background:transparent}
.drivers-photo{left:593px;top:1691px;width:434px;height:380px;border-radius:240px 0 240px 0;background:linear-gradient(130deg,#d9dde0 0%,#8d8478 35%,#b4532e 60%,#7c3a22 80%,#3a3431 100%)}

.looking{left:0;top:2092px;width:1200px;height:591px}
.looking-photo{left:0;top:0;width:1200px;height:591px;background:linear-gradient(100deg,#5f7a3c 0%,#7c9a56 18%,#3f7248 35%,#9aa4ad 55%,#a9b2ba 75%,#c3c9cf 100%)}
.looking-title{left:737px;top:186px;color:var(--white);font-size:34px}
.checks{list-style:none}
.checks li{position:relative;padding-left:24px;font-size:12.5px;line-height:18px}
.checks li::before{content:"";position:absolute;left:0;top:2px;width:14px;height:14px;border-radius:50%;background:var(--ink)}
.checks li::after{content:"";position:absolute;left:4px;top:5px;width:6px;height:3.5px;border-left:1.6px solid var(--white);border-bottom:1.6px solid var(--white);transform:rotate(-45deg)}
.checks.light li{color:var(--white)}
.checks.light li::before{background:var(--white)}
.checks.light li::after{border-color:var(--ink)}
.looking-list{left:737px;top:240px;width:390px}
.looking-list li{margin-bottom:17px}
.looking-btn{left:737px;top:384px;width:131px;height:45px;background:var(--white)}

.why-title{left:173px;top:2728px}
.why-list{left:173px;top:2790px;width:420px}
.why-list li{margin-bottom:17px;color:var(--ink-soft)}
.why-btn{left:173px;top:2918px;width:161px;height:45px;background:transparent}
.why-photo{left:588px;top:2695px;width:436px;height:314px;border-radius:24px;background:radial-gradient(ellipse at 50% 55%,#6f87ad 0%,#8ea2c0 35%,#d8dde4 62%,#ffffff 80%)}

.pricing-title{left:0;top:3058px;width:1200px;text-align:center}
.plan{position:absolute;top:3123px;width:242px;height:451px;background:var(--white);border-radius:16px;box-shadow:0 6px 22px rgba(0,0,0,.08);overflow:hidden}
.plan-head{height:86px;display:flex;flex-direction:column;align-items:center;justify-content:center;background:var(--ink);color:var(--white)}
.plan-head.sand{background:var(--sand);color:var(--ink)}
.plan-head h3{font-family:'Bebas Neue',sans-serif;font-weight:400;font-size:27px;line-height:1}
.plan-head span{font-family:'Bebas Neue',sans-serif;font-size:15px;margin-top:4px}
.plan-for{font-family:'Bebas Neue',sans-serif;font-size:15px;text-align:center;margin-top:18px}
.plan .checks{margin:16px 0 0 26px}
.plan .checks li{font-size:9.5px;line-height:15px;margin-bottom:15px;color:var(--ink)}
.plan .checks li::before{top:1px}
.plan .checks li::after{top:4px}
.plan .checks li b{font-weight:600;text-transform:uppercase;font-size:8.5px;display:block}
.plan .checks li em{font-style:normal;color:var(--muted)}
.plan-est{font-family:'Bebas Neue',sans-serif;font-size:14px;text-align:center;margin-top:6px}
.plan .btn{left:67px;top:382px;width:107px;height:43px;background:transparent;font-size:11px}

.audit-title{left:0;top:3688px;width:1200px;text-align:center}
.audit-sub{left:0;top:3766px;width:1200px;text-align:center;font-family:'Bebas Neue',sans-serif;font-size:13.5px;color:var(--ink)}
.audit-btn{left:510px;top:3798px;width:178px;height:44px;background:transparent}
.audit-art{left:82px;top:3700px;width:300px;height:346px;border-radius:20px;background:linear-gradient(180deg,#ffffff 0%,#f1f1f1 100%)}
.audit-pins{left:965px;top:3830px;width:160px;height:130px;border-radius:20px;background:#f3f3f3}

.footer{left:0;top:4046px;width:1200px;height:408px;background:var(--ink)}
.footer-brand{left:86px;top:4195px;display:flex;align-items:center;gap:18px}
.footer-brand .brand-square{background:var(--white);width:72px;height:72px}
.footer-brand .brand-name{color:var(--white);font-size:24px;line-height:1.25;font-weight:500;border-left:2px solid var(--white);padding-left:16px}
.fcol h4{font-family:'Bebas Neue',sans-serif;font-weight:400;font-size:22px;color:var(--white);letter-spacing:.4px}
.fcol ul{list-style:none;margin-top:16px}
.fcol li{font-size:12px;color:#d5d7da;line-height:27px}
.fcol-company{left:425px;top:4140px}
.fcol-info{left:610px;top:4140px}
.fcol-signup{left:784px;top:4140px}
.signup{left:783px;top:4186px;width:324px;height:48px;background:var(--white);border-radius:8px;border:2px solid var(--white)}
.signup span{position:absolute;left:18px;top:14px;font-size:12px;color:var(--muted)}
.signup .btn{left:235px;top:3px;width:83px;height:38px;background:var(--ink);color:var(--white);font-size:11px}
.social{position:absolute;width:36px;height:36px;border:2px solid var(--white);border-radius:50%;top:4263px}
.copyright{left:0;top:4400px;width:1200px;text-align:center;font-family:'Bebas Neue',sans-serif;font-size:14px;color:var(--white)}
.to-top{left:1125px;top:4391px;width:40px;height:40px;border-radius:50%;background:#454c56;display:flex;align-items:center;justify-content:center}
</style>
</head>
<body>

<div class="photo hero-photo" role="img" aria-label="Truck driver in sunglasses and cap leaning out of a red truck cab"></div>
<svg class="abs" style="left:0;top:0" width="1200" height="685" viewBox="0 0 1200 685">
  <path d="M0 685 L760 685 C880 685 900 560 1040 560 C1110 560 1160 555 1200 550 L1200 685 Z" fill="#ecdcc0"/>
</svg>
<svg class="header-tab" width="340" height="90" viewBox="0 0 340 90">
  <path d="M0 0 H340 C270 0 270 85 190 85 H0 Z" fill="#ffffff"/>
</svg>
<div class="brand"><div class="brand-square"></div><div class="brand-name">Harbor<br>Field<br>Staffing</div></div>
<nav class="nav">
  <a class="active">Home</a><a>About</a><a>Services</a><a>For Drivers</a><a>Contact</a>
</nav>
<div class="btn nav-cta"><span class="dot"></span>Find a Driver</div>

<div class="abs hero-card"></div>
<div class="abs hero-rule"></div>
<h1 class="abs display hero-title">Welcome<br>Harbor Field<br>Staffing</h1>
<p class="abs display hero-sub">Your trusted partner in providing skilled truck drivers for central California's agricultural trucking industry.</p>
<div class="btn btn-sand hero-btn">Join Our Team</div>
<div class="arrow arrow-prev"><svg width="10" height="10" viewBox="0 0 10 10"><path d="M6.5 1.5 L3 5 L6.5 8.5" stroke="#fff" stroke-width="1.6" fill="none"/></svg></div>
<div class="arrow arrow-next"><svg width="10" height="10" viewBox="0 0 10 10"><path d="M3.5 1.5 L7 5 L3.5 8.5" stroke="#2f3640" stroke-width="1.6" fill="none"/></svg></div>

<section class="abs about"></section>
<svg class="abs" style="left:0;top:1100px" width="1200" height="104" viewBox="0 0 1200 104">
  <path d="M150 104 C230 104 240 40 340 40 H930 C1010 40 1020 104 1100 104 Z" fill="#ffffff"/>
</svg>
<div class="photo about-img1" role="img" aria-label="Green utility truck in a corn field"></div>
<div class="photo about-img2" role="img" aria-label="Forage harvester loading a trailer in a corn field"></div>
<h2 class="abs section-title about-title">About Harbor Field<br>Staffing</h2>
<p class="abs body-copy about-copy">At Harbor Field Staffing, we pride ourselves on being more than just a staffing agency. Based in the heart of Central California, we specialize in providing experienced truck drivers to the agricultural trucking industry. With deep roots in agriculture and transportation, our team understands the unique needs of both drivers and businesses.</p>
<div class="btn btn-outline about-btn">Learn More</div>

<h2 class="abs section-title services-title">Our Services</h2>
<div class="service" style="left:138px">
  <div class="service-icon"><div role="img" aria-label="Icon of a team of workers"></div></div>
  <h3>Tailored Staffing<br>Solutions</h3>
  <p>We provide qualified, experienced truck drivers for businesses throughout Central California. Whether you need temporary...</p>
</div>
<div class="service featured" style="left:453px">
  <div class="service-icon"><div role="img" aria-label="Icon of a driver beside a truck"></div></div>
  <h3>Driver<br>Recruitment</h3>
  <p>We carefully vet and select drivers who meet the highest standards of safety, reliability, &amp; professionalism. Our recruitment process...</p>
</div>
<div class="service" style="left:768px">
  <div class="service-icon"><div role="img" aria-label="Icon of a support agent with a chat bubble"></div></div>
  <h3>Our Ongoing<br>Support</h3>
  <p>We don't just place drivers; we support them throughout their employment journey. From training to compliance checks...</p>
</div>

<h2 class="abs section-title drivers-title">For Drivers Drive<br>Your Legacy Forward</h2>
<p class="abs body-copy drivers-copy">At Harbor Field Staffing, we value the hard work and dedication of our drivers. Whether you're a seasoned professional or new to the industry, we offer opportunities that allow you to grow and thrive in the agricultural trucking sector.</p>
<div class="btn btn-outline drivers-btn">Find a Driver</div>
<div class="photo drivers-photo" role="img" aria-label="Driver in a plaid shirt holding the steering wheel inside a truck cab"></div>

<section class="abs looking">
  <div class="photo looking-photo" role="img" aria-label="Green agricultural truck with trailer on a road beside a corn field"></div>
  <svg class="abs" style="left:0;top:0" width="1200" height="591" viewBox="0 0 1200 591">
    <path d="M0 0 H1200 V72 H570 C480 72 470 0 380 0 Z" fill="#ffffff"/>
    <path d="M0 519 H820 C905 519 915 591 1000 591 H0 Z" fill="#ffffff"/>
  </svg>
  <h2 class="abs display looking-title">What We're Looking For</h2>
  <ul class="abs checks light looking-list">
    <li>Valid CDL and a clean driving record.</li>
    <li>Experience in agricultural trucking preferred, but we're willing to train motivated individuals.</li>
    <li>Strong work ethic and commitment to safety.</li>
  </ul>
  <div class="btn looking-btn">Apply Now</div>
</section>

<h2 class="abs section-title why-title">Why Choose Us?</h2>
<ul class="abs checks why-list">
  <li>Deep understanding of the agricultural trucking industry.</li>
  <li>Personalized service tailored to your specific needs.</li>
  <li>Experienced, reliable, and safety-focused drivers.</li>
</ul>
<div class="btn btn-outline why-btn">Request Staffing</div>
<div class="photo why-photo" role="img" aria-label="Blue semi truck cab"></div>

<h2 class="abs section-title pricing-title">Pricing Plans</h2>

<div class="plan" style="left:88px">
  <div class="plan-head"><h3>Essential</h3><span>$1,500/ Month</span></div>
  <div class="plan-for">Best For:</div>
  <ul class="checks">
    <li><b>Hiring Need:</b><em>1-10 drivers/month</em></li>
    <li><b>Fleet Size:</b><em>1-100 trucks</em></li>
    <li><b>Number of Recruiters:</b><em>1+</em></li>
    <li><b>Monthly Advertising Budget</b><em>$2,000/month</em></li>
  </ul>
  <div class="plan-est">Estimated Number of Candidates</div>
  <div class="btn btn-outline">Get a Demo</div>
</div>
<div class="plan" style="left:348px">
  <div class="plan-head sand"><h3>Basic</h3><span>$2,500/ Month</span></div>
  <div class="plan-for">Best For:</div>
  <ul class="checks">
    <li><b>Hiring Need:</b><em>10-20 drivers/month</em></li>
    <li><b>Fleet Size:</b><em>100-2500 trucks</em></li>
    <li><b>Number of Recruiters:</b><em>2+</em></li>
    <li><b>Monthly Advertising Budget</b><em>$5,000/month</em></li>
  </ul>
  <div class="plan-est">Estimated Number of Candidates</div>
  <div class="btn btn-outline">Get a Demo</div>
</div>
<div class="plan" style="left:608px">
  <div class="plan-head"><h3>Advanced</h3><span>$6,000/ Month</span></div>
  <div class="plan-for">Best For:</div>
  <ul class="checks">
    <li><b>Hiring Need:</b><em>20-30 drivers/month</em></li>
    <li><b>Fleet Size:</b><em>250-500 trucks</em></li>
    <li><b>Number of Recruiters:</b><em>3+</em></li>
    <li><b>Monthly Advertising Budget</b><em>$20,000/month</em></li>
  </ul>
  <div class="plan-est">Estimated Number of Candidates</div>
  <div class="btn btn-outline">Get a Demo</div>
</div>
<div class="plan" style="left:868px">
  <div class="plan-head sand"><h3>Enterprise</h3><span>On Request</span></div>
  <div class="plan-for">Best For:</div>
  <ul class="checks">
    <li><b>Hiring Need:</b><em>30 drivers/month</em></li>
    <li><b>Fleet Size:</b><em>500+ trucks</em></li>
    <li><b>Number of Recruiters:</b><em>5+</em></li>
    <li><b>Monthly Advertising Budget</b><em>Unlimited</em></li>
  </ul>
  <div class="plan-est">Estimated Number of Candidates</div>
  <div class="btn btn-outline">Get a Demo</div>
</div>

<div class="photo audit-art" role="img" aria-label="Line illustration of a truck with floating dollar coins"></div>
<div class="photo audit-pins" role="img" aria-label="Line illustration of map location pins along a route"></div>
<h2 class="abs section-title audit-title">Hesitating About Picking<br>The Right Package?</h2>
<p class="abs audit-sub">Request a free audit and let our truck driver recruiting agency review your online presence</p>
<div class="btn btn-outline audit-btn">Request a Free Audit</div>

<footer class="abs footer"></footer>
<div class="abs footer-brand"><div class="brand-square"></div><div class="brand-name">Harbor<br>Field<br>Staffing</div></div>
<div class="abs fcol fcol-company">
  <h4>Company</h4>
  <ul><li>Find A Job</li><li>Driver Jobs Region</li><li>Find A Driver</li><li>Apply Online</li><li>Blog</li></ul>
</div>
<div class="abs fcol fcol-info">
  <h4>Information</h4>
  <ul><li>FAQs</li><li>Reviews</li><li>Privacy Policy</li><li>Terms of Service</li><li>Refund Policy</li></ul>
</div>
<div class="abs fcol fcol-signup"><h4>Sign Up For Exclusive Offer</h4></div>
<div class="abs signup"><span>Enter email address</span><div class="btn">Submit</div></div>
<div class="social" style="left:786px"></div>
<div class="social" style="left:832px"></div>
<div class="social" style="left:878px"></div>
<div class="social" style="left:924px"></div>
<p class="abs copyright">© 2024 Harbor Field Staffing. All Rights Reserved</p>
<div class="abs to-top"><svg width="10" height="10" viewBox="0 0 10 10"><path d="M1.5 6.5 L5 3 L8.5 6.5" stroke="#fff" stroke-width="1.6" fill="none"/></svg></div>

</body>
</html>
```